Hollowmere Farm Promotional Leaflet

The team at Hollowmere Farm can help with every aspect of managing and enhancing your home from housekeeping and professional cleaning, laundry and ironing to providing chic and contemporary flower arrangements and even food for your pets!We take pride in providing high-end, consistent and reliable professional services bespoke to you. Whether you are a busy professional working long hours, a stay-at home parent or retired; having professional help in the home gives you time to spend on the things you enjoy.We are providing a very upmarket, highly professional service and need an A5 promotional leaflet to be designed. Please refer to www.hollowmerefarm-example.co.uk and see the section on 'Home Management'The leaflet should incorporate the Hollowmere Farm logo without the 'tipi', and any suitable photography images used on the home page of the website or the 'home management' section.

Target Market(s)

high-end, affluent owners of luxury homes

Industry/Entity Type

Farm

Contact Information for Business Card

The business card design needs to be suitable for use across all of Hollowmere Farm businesses, specifically:
Hollowmere Farm Home Management - otherwise known as Hollowmere Farm @ Home (this uses the typographical logo
Hollowmere Farm Weddings & Events - this uses the 'tipi' logo

Requirements
Must have
• Design in keeping with the look and feel of the logo and website design
• www.hollowmerefarm-example.co.uk

```html
<!DOCTYPE html>
<html lang="en">
<head>
<meta charset="utf-8">
<title>Hollowmere Farm Home Management Leaflet</title>
<link rel="stylesheet" href="https://fonts.googleapis.com/css2?family=Great+Vibes&family=Lato:wght@400;700&family=Oswald:wght@600&display=swap">
<style>
  :root {
    --pink: #d9245e;
    --pink-soft: #ec6aa6;
    --gold: #e2b865;
    --ink: #3a3a3a;
    --paper: #ffffff;
    --backdrop: #e4e6ea;
  }
  * { box-sizing: border-box; margin: 0; padding: 0; }
  html, body { width: 1200px; height: 1200px; overflow: hidden; }
  body {
    background: var(--backdrop);
    font-family: "Lato", Arial, sans-serif;
    color: var(--ink);
  }
  .leaflet {
    position: absolute;
    left: 204px; top: 40px;
    width: 792px; height: 1120px;
    background: var(--paper);
    overflow: hidden;
    box-shadow: 0 6px 24px rgba(0,0,0,.15);
  }
  .hero-photo {
    position: absolute; left: 260px; top: 0;
    width: 532px; height: 340px;
    background: linear-gradient(90deg, #ffffff 0%, #d9d2c8 22%, #a89d90 50%, #8c8276 75%, #bdb4a8 100%);
  }
  .shapes { position: absolute; inset: 0; }
  .brand {
    position: absolute; left: 48px; top: 150px;
    display: flex; align-items: center; gap: 10px;
    font-weight: 700; font-size: 30px; color: var(--pink-soft);
  }
  .brand-dot { width: 14px; height: 14px; border-radius: 50%; background: var(--gold); }
  .kitchen-photo {
    position: absolute; left: 550px; top: 270px;
    width: 180px; height: 180px; border-radius: 50%;
    background: radial-gradient(circle at 50% 40%, #e9e6e1, #9a9690 55%, #3f4a4a 100%);
  }
  .headline { position: absolute; left: 56px; top: 390px; }
  .headline-script {
    font-family: "Great Vibes", cursive; font-size: 62px; line-height: 1;
    color: var(--pink-soft);
  }
  .headline-title {
    font-family: "Oswald", sans-serif; font-weight: 600; font-size: 44px;
    color: var(--gold); letter-spacing: .5px; line-height: 1.1;
  }
  .intro {
    position: absolute; left: 60px; top: 545px; width: 340px;
    font-size: 16px; line-height: 1.35;
  }
  .about {
    position: absolute; left: 470px; top: 470px; width: 290px;
    font-size: 14px; line-height: 1.35;
  }
  .about p + p { margin-top: 6px; }
  .benefits {
    position: absolute; left: 500px; top: 640px; width: 265px;
    list-style: none; font-size: 14px; font-weight: 700; line-height: 1.3;
  }
  .benefits li { position: relative; padding-left: 18px; margin-bottom: 10px; }
  .benefits li::before {
    content: ""; position: absolute; left: 0; top: 6px;
    width: 7px; height: 7px; border-radius: 50%; background: var(--pink);
  }
  .coverage {
    position: absolute; left: 500px; top: 880px; width: 270px;
    font-size: 13px; line-height: 1.35;
  }
  .services {
    position: absolute; left: 36px; top: 722px; width: 420px;
    list-style: none; color: #fff; font-weight: 700; font-size: 16px; line-height: 1.2;
  }
  .services li { display: flex; align-items: center; gap: 14px; min-height: 38px; margin-bottom: 4px; }
  .service-thumb {
    flex: none; width: 38px; height: 38px; border-radius: 50%;
    background: radial-gradient(circle, #d8d2ca, #8d857c);
    border: 2px solid #fff;
  }
  .service-spacer { flex: none; width: 38px; }
  .contact {
    position: absolute; left: 545px; top: 992px; width: 240px;
    font-size: 13px; color: var(--ink); line-height: 1.35;
  }
  .contact-lead { font-weight: 700; margin-bottom: 8px; }
  .contact-row { display: flex; align-items: center; gap: 7px; margin-bottom: 4px; font-size: 12.5px; white-space: nowrap; }
  .contact-row svg { flex: none; }
</style>
</head>
<body>
<main class="leaflet">
  <div class="hero-photo" role="img" aria-label="Photo of an elegant grey living room with sofas, fireplace and chandelier"></div>

  <svg class="shapes" width="792" height="1120" viewBox="0 0 792 1120" aria-hidden="true">
    <path d="M0,332 Q400,392 792,318 L792,1120 L0,1120 Z" fill="#ffffff"/>
    <path d="M0,300 Q400,360 792,290 L792,318 Q400,392 0,332 Z" fill="var(--pink)"/>
    <path d="M0,340 Q400,400 792,326 L792,338 Q400,414 0,352 Z" fill="var(--gold)"/>
    <rect x="440" y="978" width="352" height="142" fill="var(--gold)"/>
    <path d="M0,682 C120,642 330,632 420,692" fill="none" stroke="var(--gold)" stroke-width="10"/>
    <path d="M0,690 C120,650 330,640 420,700 C500,760 470,880 478,960 C484,1040 500,1090 520,1120 L0,1120 Z" fill="var(--pink)"/>
    <circle cx="640" cy="360" r="104" fill="#fff" stroke="var(--pink)" stroke-width="2"/>
    <circle cx="640" cy="360" r="96" fill="none" stroke="var(--gold)" stroke-width="8"/>
  </svg>

  <div class="kitchen-photo" role="img" aria-label="Round photo of a modern kitchen with range cooker and dark cabinets"></div>

  <div class="brand"><span class="brand-dot"></span>Hollowmere Farm</div>

  <header class="headline">
    <div class="headline-script">Hollowmere Farm</div>
    <div class="headline-title">HOME MANAGEMENT</div>
  </header>

  <p class="intro">The team @ Hollowmere Farm can help with every aspect of managing and enhancing your home including:</p>

  <div class="about">
    <p>We take pride in providing high-end, consistent and reliable professional services bespoke to you.</p>
    <p>Coming home to a beautiful environment and being able to relax and enjoy your time is something we all deserve.</p>
  </div>

  <ul class="benefits">
    <li>Satisfaction guaranteed</li>
    <li>Professional staff you can trust &amp; rely on</li>
    <li>Competitive rates</li>
    <li>CRB checked and referenced</li>
    <li>Member of the Home Staffing Standards Guild</li>
    <li>Fully Insured</li>
  </ul>

  <p class="coverage">We look after our clients' homes and holiday lets across South Somerset and surrounding areas.</p>

  <ul class="services">
    <li><span class="service-thumb" role="img" aria-label="Small photo of a cleaned living room"></span>Regular housekeeping and professional cleaning</li>
    <li><span class="service-thumb" role="img" aria-label="Small photo of a tidy interior"></span>Exit cleans</li>
    <li><span class="service-thumb" role="img" aria-label="Small photo of a bright kitchen"></span>One-off seasonal / party / building work cleans</li>
    <li><span class="service-thumb" role="img" aria-label="Small photo of folded laundry"></span>Laundry and ironing</li>
    <li><span class="service-thumb" role="img" aria-label="Small photo of a flower arrangement"></span>Chic and contemporary flower arrangements</li>
    <li><span class="service-spacer"></span>Car valeting</li>
    <li><span class="service-spacer"></span>Pet food delivery</li>
    <li><span class="service-spacer"></span>Dry cleaning</li>
  </ul>

  <div class="contact">
    <p class="contact-lead">Contact us to arrange a home visit &amp; quotation:</p>
    <div class="contact-row">
      <svg width="16" height="16" viewBox="0 0 16 16"><circle cx="8" cy="8" r="8" fill="var(--pink)"/><rect x="4" y="5" width="8" height="6" fill="none" stroke="#fff" stroke-width="1.2"/><path d="M4,5 L8,8.5 L12,5" fill="none" stroke="#fff" stroke-width="1.2"/></svg>
      info@hollowmerefarm-example.co.uk
    </div>
    <div class="contact-row">
      <svg width="16" height="16" viewBox="0 0 16 16"><path d="M4,2 L6.5,2 L7.5,5 L6,6.2 C6.8,8 8,9.2 9.8,10 L11,8.5 L14,9.5 L14,12 C14,13 13,14 12,14 C7,13.5 2.5,9 2,4 C2,3 3,2 4,2 Z" fill="var(--pink)"/></svg>
      07700 900123
    </div>
    <div class="contact-row">
      <svg width="16" height="16" viewBox="0 0 16 16"><circle cx="8" cy="8" r="8" fill="var(--pink)"/><circle cx="8" cy="8" r="5" fill="none" stroke="#fff" stroke-width="1"/><ellipse cx="8" cy="8" rx="2.2" ry="5" fill="none" stroke="#fff" stroke-width="1"/><path d="M3,8 H13" stroke="#fff" stroke-width="1"/></svg>
      www.hollowmerefarm-example.co.uk
    </div>
  </div>
</main>
</body>
</html>
```